Come Play With Us!!! We are the Elite

We need a hiring flyer to hand out to potential recruits.
Please promote our social pages.
Something attractive, and informative with calls to action to contact us.
Please promote for people to follow us on social media.
We would like to list the following advantages to work here:
• Industry Leading Compensation
• Structured Career Advancement
• Safe Work Environment
• Work Promise Policy (Full Time Staff)
• Health & Dental Benefits
• Paid Training Programs
• Paid Clothing Allowance
• Paid Boot Allowance
• Positive Culture
• Progressive Culture
• Equal Opportunity Employer
• Veteran Friendly Employer
• New Equipment
• Paid Leadership Training
• Transparent Communication
• Community Focused
• Prestigious Clientele
• Local Work
• Focused on using industry leading tech
• Tool Purchase Program
• Family Atmosphere
• Team Events (Sports games, Lunches, Get togethers, Etc)
• Work Life balance
• Daily On Call Snow Pay
- Sick Pay
- Positive reputation
• Bonus’s available:
o Winter Shift Premium
o Referral Bonus
o Project Incentives
Current Positions open:
- Winter Crew Members
- Salt Truck Driver/Operator (AZ/DZ/AR)
- Winter Equipment Operators
- Construction Foreperson
Landscape and Construction

```html
<!DOCTYPE html>
<html lang="en">
<head>
<meta charset="utf-8">
<title>Riverbend Contracting Group – We Are Hiring</title>
<link rel="stylesheet" href="https://fonts.googleapis.com/css2?family=Montserrat:wght@300&family=Roboto:wght@400;500;700;900&display=swap">
<style>
  :root{
    --green-dark:#2f7a1c;
    --green-mid:#3f9325;
    --green-lime:#8cc63f;
    --green-bright:#9be04a;
    --ink:#1c1c1c;
    --grey-band:#ececec;
    --footer:#3a3a3a;
    --white:#ffffff;
  }
  *{box-sizing:border-box;margin:0;padding:0}
  html,body{width:800px;height:1200px;overflow:hidden;background:#fff}
  body{font-family:"Roboto",Arial,sans-serif;color:var(--ink)}
  .flyer{position:relative;width:800px;height:1200px;background:var(--white);overflow:hidden}

  /* header */
  .brand{position:absolute;left:45px;top:92px;display:flex;align-items:center;gap:14px}
  .brand-dot{width:52px;height:52px;border-radius:50%;background:var(--green-dark)}
  .brand-name{font-family:"Montserrat",sans-serif;font-weight:300;font-size:25px;line-height:1.1;letter-spacing:2px;color:var(--ink)}

  .hero-photo{position:absolute;left:298px;top:12px;width:502px;height:468px;
    border-top:5px solid var(--green-lime);border-left:5px solid var(--green-lime);
    border-radius:300px 0 0 0 / 320px 0 0 0;
    background:linear-gradient(180deg,#c9ced6 0%,#9aa6b3 45%,#4e6a3a 72%,#3c5d28 100%)}

  .hiring-band{position:absolute;left:0;top:206px;width:424px;height:274px;
    background:var(--green-lime);border-radius:0 140px 140px 0 / 0 137px 137px 0}
  .hiring-core{position:absolute;left:0;top:6px;width:414px;height:262px;
    background:linear-gradient(135deg,var(--green-mid),var(--green-dark));
    border-radius:0 132px 132px 0 / 0 131px 131px 0}
  .hiring-title{position:absolute;left:46px;top:34px;font-weight:900;line-height:.92;letter-spacing:-3px}
  .hiring-title .line1{display:block;font-size:84px;color:var(--white)}
  .hiring-title .line2{display:block;font-size:96px;color:var(--green-bright)}

  /* positions */
  .positions{position:absolute;left:0;top:512px;width:800px;height:172px;background:var(--grey-band);
    border-top:2px solid var(--green-dark);border-bottom:2px solid var(--green-dark)}
  .section-pill{position:absolute;left:222px;top:494px;width:373px;height:40px;border-radius:20px;
    background:linear-gradient(180deg,var(--green-mid),var(--green-dark));border:3px solid var(--green-lime);
    color:var(--white);font-weight:700;font-size:22px;text-align:center;line-height:34px;letter-spacing:.3px}
  .job{position:absolute;top:548px;width:180px;text-align:center;font-weight:500;font-size:13px;line-height:1.25}
  .job-photo{display:block;width:136px;height:84px;margin:0 auto 10px;border:3px solid var(--green-lime)}
  .job-photo.crew{background:linear-gradient(160deg,#8fa3b5,#c7b73a 60%,#4c5d3a)}
  .job-photo.salt{background:linear-gradient(160deg,#b9c2cc,#d46a22 55%,#5a5a5a)}
  .job-photo.equip{background:linear-gradient(160deg,#2a6fb5,#1f2a3a 55%,#c9d6e0)}
  .job-photo.fore{background:linear-gradient(160deg,#9a7b5c,#f06a1c 50%,#d9d9d9)}

  /* advantages */
  .advantages{position:absolute;left:45px;top:722px;width:710px;height:196px;border:3px solid var(--green-lime);border-radius:12px}
  .adv-title{position:absolute;left:185px;top:-16px;padding:0 22px;background:var(--white);
    font-weight:700;font-size:23px;color:var(--ink);letter-spacing:.2px}
  .adv-title em{font-style:normal;color:var(--green-lime)}
  .adv-list{position:absolute;top:22px;list-style:none;font-size:12.2px;line-height:18px;white-space:nowrap}
  .adv-list li{position:relative;padding-left:13px}
  .adv-list li::before{content:"";position:absolute;left:0;top:6px;width:5px;height:5px;border-radius:50%;background:var(--green-lime)}
  .adv-list.col1{left:20px}.adv-list.col2{left:262px}.adv-list.col3{left:462px;top:20px}
  .adv-list li.two-line{line-height:13px;padding-top:2px}

  /* bonuses */
  .bonus-band{position:absolute;left:255px;top:929px;width:545px;height:128px;
    background:linear-gradient(90deg,var(--green-mid),var(--green-lime));border-radius:64px 0 0 64px}
  .bonus-pill{position:absolute;left:13px;top:23px;width:142px;height:84px;border-radius:42px;background:var(--white);
    display:flex;align-items:center;justify-content:center;text-align:center;font-weight:500;font-size:25px;line-height:1}
  .bonus-item{position:absolute;top:18px;width:110px;text-align:center;color:var(--white);font-weight:500;font-size:14.5px;line-height:1.2}
  .bonus-item svg{display:block;margin:0 auto 8px}
  .divider{position:absolute;top:22px;height:86px;border-left:2px dotted rgba(255,255,255,.8)}

  /* footer */
  .footer{position:absolute;left:0;top:1067px;width:800px;height:133px;background:var(--footer)}
  .loader-photo{position:absolute;left:0;top:924px;width:287px;height:276px;
    clip-path:polygon(30% 0,100% 25%,100% 100%,0 100%,0 18%);
    background:linear-gradient(160deg,#3a3a3a 0%,#e8641c 45%,#1f1f1f 100%)}
  .call{position:absolute;left:312px;top:1088px;color:var(--white)}
  .call-label{display:block;color:var(--green-lime);font-weight:500;font-size:25px}
  .call-phone{display:flex;align-items:center;gap:6px;margin-top:6px;font-weight:500;font-size:22px;white-space:nowrap}
  .contact{position:absolute;left:505px;top:1101px;list-style:none;color:var(--white);font-weight:500;font-size:15px;line-height:28px;white-space:nowrap}
  .contact li{display:flex;align-items:center;gap:8px}
</style>
</head>
<body>
<main class="flyer">
  <div class="hero-photo" role="img" aria-label="Smiling crew member in a cap holding a power drill in front of a blue tractor and a hiring sign under a cloudy sky"></div>

  <header class="brand">
    <span class="brand-dot"></span>
    <span class="brand-name">RIVERBEND<br>CONTRACTING<br>GROUP</span>
  </header>

  <section class="hiring-band">
    <div class="hiring-core">
      <h1 class="hiring-title"><span class="line1">WE ARE</span><span class="line2">HIRING</span></h1>
    </div>
  </section>

  <section class="positions" aria-label="Current positions open"></section>
  <h2 class="section-pill">CURRENT POSITIONS OPEN</h2>
  <div class="job" style="left:37px"><span class="job-photo crew" role="img" aria-label="Winter crew in high-visibility vests"></span>Winter Crew Members</div>
  <div class="job" style="left:218px"><span class="job-photo salt" role="img" aria-label="Orange wheel loader beside a salt pile"></span>Salt Truck Driver/<br>Operator (AZ/DZ/AR)</div>
  <div class="job" style="left:400px"><span class="job-photo equip" role="img" aria-label="Operator seated in an equipment cab"></span>Winter Equipment<br>Operators</div>
  <div class="job" style="left:582px"><span class="job-photo fore" role="img" aria-label="Foreperson in orange safety gear at a job site"></span>Construction Foreperson</div>

  <section class="advantages">
    <h2 class="adv-title"><em>ADVANTAGES</em> TO WORK HERE</h2>
    <ul class="adv-list col1">
      <li>Industry Leading Compensation</li>
      <li>Structured Career Advancement</li>
      <li>Safe Work Environment</li>
      <li>Work Promise Policy (Full Time Staff)</li>
      <li>Health &amp; Dental Benefits</li>
      <li>Paid Training Programs</li>
      <li>Paid Clothing Allowance</li>
      <li>Transparent Communication</li>
      <li>Community Focused</li>
    </ul>
    <ul class="adv-list col2">
      <li>Paid Boot Allowance</li>
      <li>Positive Culture</li>
      <li>Progressive Culture</li>
      <li>Equal Opportunity Employer</li>
      <li>Veteran Friendly Employer</li>
      <li>New Equipment</li>
      <li>Paid Leadership Training</li>
      <li class="two-line">Team Events (Sports games,<br>Lunches, Get togethers, Etc)</li>
    </ul>
    <ul class="adv-list col3">
      <li>Local Work</li>
      <li>Focused on using industry leading tech</li>
      <li>Tool Purchase Program</li>
      <li>Family Atmosphere</li>
      <li>Work Life balance</li>
      <li>Daily On Call Snow Pay</li>
      <li>Sick Pay</li>
      <li>Positive reputation</li>
      <li>Prestigious Clientele</li>
    </ul>
  </section>

  <footer class="footer"></footer>

  <section class="bonus-band">
    <div class="bonus-pill">Bonus’s<br>Available</div>
    <span class="divider" style="left:175px"></span>
    <div class="bonus-item" style="left:180px">
      <svg width="30" height="34" viewBox="0 0 30 34" fill="none" stroke="#fff" stroke-width="2.2"><circle cx="15" cy="13" r="10"/><path d="M15 8l1.6 3.3 3.6.5-2.6 2.5.6 3.6-3.2-1.7-3.2 1.7.6-3.6-2.6-2.5 3.6-.5z" fill="#fff" stroke="none"/><path d="M9 21l-3 11 5-2 3 3 1-9M21 21l3 11-5-2-3 3"/></svg>
      Winter<br>Shift Premium
    </div>
    <span class="divider" style="left:300px"></span>
    <div class="bonus-item" style="left:293px">
      <svg width="34" height="34" viewBox="0 0 34 34" fill="none" stroke="#fff" stroke-width="2.2"><circle cx="10" cy="9" r="5"/><path d="M2 24c0-5 4-8 8-8s8 3 8 8"/><circle cx="24" cy="17" r="5"/><path d="M16 32c0-5 4-8 8-8s8 3 8 8"/><path d="M22 4h8v6"/></svg>
      Referral<br>Bonus
    </div>
    <span class="divider" style="left:405px"></span>
    <div class="bonus-item" style="left:410px">
      <svg width="34" height="34" viewBox="0 0 34 34" fill="none" stroke="#fff" stroke-width="2.2"><rect x="10" y="4" width="20" height="26" rx="2"/><path d="M15 11h10M15 17h10M15 23h7"/><circle cx="8" cy="17" r="5" fill="#6aaf32"/></svg>
      Project<br>Incentives
    </div>
    <span class="divider" style="left:525px"></span>
  </section>

  <div class="loader-photo" role="img" aria-label="Orange and black wheel loader"></div>

  <div class="call">
    <span class="call-label">Call Us Now!</span>
    <span class="call-phone">
      <svg width="20" height="20" viewBox="0 0 24 24" fill="#8cc63f"><path d="M6.6 10.8a15 15 0 006.6 6.6l2.2-2.2a1 1 0 011-.25 11.4 11.4 0 003.6.57 1 1 0 011 1V20a1 1 0 01-1 1A17 17 0 013 4a1 1 0 011-1h3.5a1 1 0 011 1c0 1.25.2 2.45.57 3.57a1 1 0 01-.25 1z"/></svg>
      +123 456 7890
    </span>
  </div>
  <ul class="contact">
    <li><svg width="20" height="20" viewBox="0 0 24 24" fill="none" stroke="#8cc63f" stroke-width="2"><circle cx="12" cy="12" r="10"/><path d="M2 12h20M12 2c3 3 3 17 0 20M12 2c-3 3-3 17 0 20"/></svg>www.riverbendcontracting.com</li>
    <li><svg width="20" height="16" viewBox="0 0 24 18" fill="none" stroke="#8cc63f" stroke-width="2"><rect x="1" y="1" width="22" height="16"/><path d="M1 1l11 9 11-9"/></svg>info@riverbendcontracting.com</li>
  </ul>
</main>
</body>
</html>
```